Zentro - revolutionary mobile payment

The app is a P2P money trasfert, without the using of credit card or bank circuits it can transfer electronic money from one person to another consumers simply and immediatelly.
You can use the color you want, but the message we need to transert to consumer is simplicity, safety and coolness.
In attach the logo of the company and the wireframe of thre page of the app.
The goal is to design the page of the app with a clear, simple and intuitive graphic.
Updates

I have upgrade the brief with important information and detail, many thanks

Target Market(s)

all the people

Industry/Entity Type

Credit Card

Requirements
Must have
• You have to design one icon for each button in the first page, (shop is: where to shop)
in the second one a new intuitive image (instead of the hand) that let the user to understand that with a simple swipe he can process the payment
Nice to have
• You can include or esxclude what you want or belive can improve user experience of the app
Should not have
• too much color, too much button or information

```html
<!DOCTYPE html>
<html lang="en">
<head>
<meta charset="utf-8">
<title>Zentro – Home</title>
<link rel="stylesheet" href="https://fonts.googleapis.com/css2?family=Lato:wght@300;400&display=swap">
<style>
  :root {
    --canvas-bg: #e9eaec;
    --status-blue: #5470a6;
    --navy: #1f3c78;
    --navy-light: #2a4a8b;
    --header-white: #ffffff;
    --profile-grey: #eceef2;
    --text-dark: #3a3f4a;
    --text-muted: #6b7080;
    --white: #ffffff;
    --avatar: #c89a82;
  }
  * { box-sizing: border-box; margin: 0; padding: 0; }
  html, body {
    width: 1200px; height: 751px; overflow: hidden;
    background: var(--canvas-bg);
    font-family: "Lato", "Helvetica Neue", Arial, sans-serif;
  }
  .app-screen {
    position: absolute; left: 410px; top: 38px;
    width: 380px; height: 675px;
    background: var(--navy);
    overflow: hidden;
    box-shadow: 0 4px 18px rgba(0,0,0,0.12);
  }
  .status-bar {
    height: 26px; background: var(--status-blue); color: var(--white);
    display: flex; align-items: center; justify-content: space-between;
    padding: 0 8px; font-size: 11px; position: relative;
  }
  .status-signal { display: flex; gap: 2px; align-items: center; }
  .status-signal span { width: 5px; height: 5px; border-radius: 50%; background: var(--white); }
  .status-time { position: absolute; left: 50%; transform: translateX(-50%); }
  .status-battery { display: flex; align-items: center; gap: 4px; }
  .battery-icon { width: 20px; height: 9px; border: 1px solid var(--white); padding: 1px; }
  .battery-icon::after { content: ""; display: block; width: 100%; height: 100%; background: var(--white); }
  .account-bar {
    height: 44px; background: var(--header-white);
    display: flex; align-items: center; justify-content: space-between;
    padding: 0 12px; color: var(--text-dark); font-size: 14px;
    background: linear-gradient(var(--status-blue) 0 0) top/100% 0 no-repeat, var(--header-white);
  }
  .settings-icon { position: absolute; right: 10px; top: 30px; }
  .profile-bar {
    height: 42px; background: var(--profile-grey);
    display: flex; align-items: center; gap: 14px; padding: 0 8px;
    color: var(--text-muted); font-size: 12px;
  }
  .profile-avatar { width: 32px; height: 32px; border-radius: 50%; background: var(--avatar); }
  .action-area {
    position: relative; height: calc(100% - 112px);
    background: linear-gradient(152deg, var(--navy-light) 0 46%, var(--navy) 46% 100%);
  }
  .action {
    position: absolute; width: 108px; text-align: center; color: var(--white);
    font-weight: 300; font-size: 25px;
  }
  .action-circle {
    width: 108px; height: 108px; border-radius: 50%; background: var(--white);
    display: flex; align-items: center; justify-content: center; margin-bottom: 10px;
  }
  .action-pay { left: 50px; top: 70px; }
  .action-ask { left: 222px; top: 30px; }
  .action-account { left: 62px; top: 330px; }
  .action-shop { left: 234px; top: 290px; }
  .action-ask .action-label, .action-shop .action-label { margin-left: 40px; }
</style>
</head>
<body>
<main class="app-screen">
  <div class="status-bar">
    <div class="status-signal"><span></span><span></span><span></span><span></span><span></span></div>
    <div class="status-time">4:39 PM</div>
    <div class="status-battery">100% <div class="battery-icon"></div></div>
  </div>
  <div class="account-bar">
    <span class="account-number">+321456780912</span>
  </div>
  <svg class="settings-icon" width="22" height="22" viewBox="0 0 24 24" fill="none" stroke="#1f3c78" stroke-width="1.6">
    <circle cx="12" cy="12" r="3.2"/>
    <path d="M12 2.5v3M12 18.5v3M2.5 12h3M18.5 12h3M5.3 5.3l2.1 2.1M16.6 16.6l2.1 2.1M5.3 18.7l2.1-2.1M16.6 7.4l2.1-2.1"/>
    <circle cx="12" cy="12" r="7"/>
  </svg>
  <div class="profile-bar">
    <div class="profile-avatar" role="img" aria-label="User profile photo"></div>
    <span class="profile-plan">Basic</span>
  </div>
  <section class="action-area">
    <div class="action action-pay">
      <div class="action-circle">
        <svg width="62" height="46" viewBox="0 0 62 46" fill="none" stroke="#1f3c78" stroke-width="2.4">
          <rect x="8" y="4" width="50" height="30"/>
          <rect x="3" y="11" width="50" height="30" fill="#fff"/>
          <rect x="8" y="16" width="40" height="20"/>
          <path d="M31 19v14M34 22c-1-1.5-6-1.5-6 1s6 1.5 6 4-5 2.5-6 1"/>
        </svg>
      </div>
      <div class="action-label">Pay</div>
    </div>
    <div class="action action-ask">
      <div class="action-circle">
        <svg width="62" height="46" viewBox="0 0 62 46" fill="none" stroke="#1f3c78" stroke-width="2.4">
          <rect x="4" y="14" width="48" height="26"/>
          <path d="M10 23h20M10 29h14M10 34h26"/>
          <path d="M50 4l5 3-12 22-5 2 0-5z"/>
        </svg>
      </div>
      <div class="action-label">Ask</div>
    </div>
    <div class="action action-account">
      <div class="action-circle">
        <svg width="60" height="48" viewBox="0 0 60 48" fill="none" stroke="#1f3c78" stroke-width="2.4">
          <rect x="4" y="4" width="52" height="40"/>
          <path d="M4 12h52"/>
          <circle cx="9" cy="8" r="1" fill="#1f3c78"/><circle cx="14" cy="8" r="1" fill="#1f3c78"/><circle cx="19" cy="8" r="1" fill="#1f3c78"/>
          <rect x="23" y="26" width="14" height="11"/>
          <path d="M26 26v-4a4 4 0 0 1 8 0v4"/>
        </svg>
      </div>
      <div class="action-label">Account</div>
    </div>
    <div class="action action-shop">
      <div class="action-circle">
        <svg width="62" height="48" viewBox="0 0 62 48" fill="none" stroke="#1f3c78" stroke-width="2.4">
          <path d="M2 10h8l6 24h30l6-18H14"/>
          <path d="M18 22h32M20 28h28M26 16v18M34 16v18M42 16v18"/>
          <circle cx="20" cy="41" r="3"/><circle cx="42" cy="41" r="3"/>
          <circle cx="46" cy="8" r="5"/>
        </svg>
      </div>
      <div class="action-label">Shop</div>
    </div>
  </section>
</main>
</body>
</html>
```